boosters

revamp current booster flyer - modernize make it look better

please use website
Brellonmotorhub.co.nz for as much as possible

i want you all to come with own wording description etc

```html
<!DOCTYPE html>
<html lang="en">
<head>
<meta charset="utf-8">
<title>Brake &amp; Clutch Boosters – Brellon Motor Hub</title>
<link href="https://fonts.googleapis.com/css2?family=Bebas+Neue&family=Poppins:ital,wght@0,400;0,500;0,600;0,700;1,400&display=swap" rel="stylesheet">
<style>
  :root {
    --yellow: #f8d40a;
    --yellow-deep: #efc600;
    --black: #111111;
    --charcoal: #232323;
    --white: #ffffff;
    --grey-bg: #a9a9a9;
    --text: #1a1a1a;
  }
  * { margin: 0; padding: 0; box-sizing: border-box; }
  html, body { width: 735px; height: 1200px; overflow: hidden; }
  body { background: var(--grey-bg); position: relative; font-family: "Poppins", sans-serif; color: var(--text); }

  .flyer {
    position: absolute; left: 0; top: 80px; width: 735px; height: 1040px;
    background: var(--white); overflow: hidden;
  }
  .flyer-backdrop { position: absolute; inset: 0; }

  .headline {
    position: absolute; left: 78px; top: 40px;
    font-family: "Bebas Neue", sans-serif; color: var(--black); line-height: 0.84;
  }
  .headline-line-1 { font-size: 124px; display: block; letter-spacing: 1px; }
  .headline-line-2 { font-size: 138px; display: block; letter-spacing: 1px; }
  .headline-tag {
    position: absolute; left: 80px; top: 261px; width: 241px; height: 68px;
    background: var(--black); border-radius: 6px; color: var(--white);
    font-family: "Bebas Neue", sans-serif; font-size: 68px; line-height: 72px; text-align: center;
  }

  .brand {
    position: absolute; left: 440px; top: 95px; width: 230px; text-align: center;
  }
  .brand-mark {
    width: 86px; height: 86px; border-radius: 50%; background: var(--white);
    margin: 0 auto 16px;
  }
  .brand-name {
    font-weight: 700; font-size: 19px; color: var(--black); letter-spacing: 0.5px;
  }

  .intro {
    position: absolute; left: 396px; top: 306px;
    font-weight: 600; font-size: 26px; line-height: 33px; color: var(--black);
  }
  .intro-rule { position: absolute; left: 396px; top: 378px; width: 88px; height: 2px; background: var(--yellow); }

  .product-photos {
    position: absolute; left: 146px; top: 385px; width: 508px; height: 235px;
    border-radius: 14px;
    background: radial-gradient(ellipse at 50% 50%, #3a3a3a 0%, #8a8a8a 55%, #f3f3f3 100%);
    opacity: 0.85;
  }

  .card {
    position: absolute; top: 641px; height: 278px; width: 299px;
    background: var(--white); border: 1.5px solid var(--black); border-radius: 16px; overflow: hidden;
  }
  .card-about { left: 61px; }
  .card-range { left: 375px; }

  .about-top { height: 141px; padding: 18px 0 0 34px; }
  .about-title { font-family: "Bebas Neue", sans-serif; font-size: 40px; line-height: 40px; color: var(--black); }
  .about-text { font-size: 17px; line-height: 22px; margin-top: 6px; }
  .about-aim {
    position: absolute; left: 0; right: 0; bottom: 0; height: 137px;
    background: var(--yellow); border-top: 1.5px solid var(--black); padding: 14px 0 0 34px;
  }
  .aim-title { font-family: "Bebas Neue", sans-serif; font-size: 38px; line-height: 40px; color: var(--black); }
  .aim-text { font-size: 17px; line-height: 22px; }
  .aim-target { position: absolute; left: 211px; top: -18px; }

  .range-list { list-style: none; padding: 24px 0 0 32px; }
  .range-list li { display: flex; align-items: center; gap: 10px; font-size: 21.5px; line-height: 42px; }
  .range-note { font-size: 21.5px; line-height: 27px; padding: 6px 0 0 32px; }

  .contact { position: absolute; top: 954px; font-size: 15px; line-height: 26px; color: var(--white); font-style: normal; }
  .contact-left { left: 58px; }
  .contact-right { left: 419px; }
  .contact-row { display: flex; align-items: center; gap: 10px; white-space: nowrap; }
  .contact-row.no-icon { padding-left: 30px; }
  .unsubscribe { font-style: italic; font-size: 12.5px; color: var(--yellow); line-height: 20px; padding-left: 30px; }
  .footer-brand {
    position: absolute; left: 340px; top: 968px; width: 66px; text-align: center;
    font-weight: 700; font-size: 11px; line-height: 14px; color: var(--white);
  }
</style>
</head>
<body>
  <main class="flyer">
    <svg class="flyer-backdrop" width="735" height="1040" viewBox="0 0 735 1040" aria-hidden="true">
      <defs>
        <linearGradient id="footer-metal" x1="0" y1="0" x2="1" y2="1">
          <stop offset="0" stop-color="#2b2b2b"/>
          <stop offset="0.5" stop-color="#161616"/>
          <stop offset="1" stop-color="#2e2e2e"/>
        </linearGradient>
      </defs>
      <path d="M0 0 H735 V290 C560 300 420 320 250 370 C140 402 60 430 0 455 Z" fill="var(--yellow)"/>
      <path d="M0 880 C250 860 520 790 735 720 V745 C520 815 250 885 0 905 Z" fill="#e4e4e4"/>
      <path d="M0 905 C250 885 520 815 735 745 V1040 H0 Z" fill="url(#footer-metal)"/>
    </svg>

    <h1 class="headline">
      <span class="headline-line-1">Brake &amp;</span>
      <span class="headline-line-2">Clutch</span>
    </h1>
    <div class="headline-tag">Boosters</div>

    <div class="brand">
      <div class="brand-mark"></div>
      <div class="brand-name">BRELLON MOTOR HUB</div>
    </div>

    <p class="intro">Suppliers and<br>repairers</p>
    <div class="intro-rule"></div>

    <div class="product-photos" role="img" aria-label="Photographs of truck boosters, clutch boosters, vacuum boosters and master cylinders"></div>

    <section class="card card-about">
      <div class="about-top">
        <h2 class="about-title">Brellon Motor Hub</h2>
        <p class="about-text">specialise in the Re-<br>Manufacture of Brakes,<br>Hoses and Cables</p>
      </div>
      <div class="about-aim">
        <svg class="aim-target" width="68" height="68" viewBox="0 0 72 72" aria-hidden="true">
          <circle cx="36" cy="36" r="33" fill="var(--yellow)" stroke="var(--black)" stroke-width="2"/>
          <circle cx="36" cy="36" r="22" fill="none" stroke="var(--black)" stroke-width="2.5"/>
          <circle cx="36" cy="36" r="10" fill="none" stroke="var(--black)" stroke-width="2"/>
          <path d="M36 4 V26 M36 46 V68 M4 36 H26 M46 36 H68" stroke="var(--black)" stroke-width="2"/>
        </svg>
        <h2 class="aim-title">Our aim is</h2>
        <p class="aim-text">to repair parts with the<br>quickest turn-around<br>times possible</p>
      </div>
    </section>

    <section class="card card-range">
      <ul class="range-list">
        <li><svg width="22" height="22" viewBox="0 0 22 22" aria-hidden="true"><circle cx="11" cy="11" r="10" fill="var(--yellow)"/><path d="M6 11.5 L9.5 15 L16 7.5" fill="none" stroke="var(--black)" stroke-width="2.4"/></svg>Truck Boosters</li>
        <li><svg width="22" height="22" viewBox="0 0 22 22" aria-hidden="true"><circle cx="11" cy="11" r="10" fill="var(--yellow)"/><path d="M6 11.5 L9.5 15 L16 7.5" fill="none" stroke="var(--black)" stroke-width="2.4"/></svg>Clutch Boosters</li>
        <li><svg width="22" height="22" viewBox="0 0 22 22" aria-hidden="true"><circle cx="11" cy="11" r="10" fill="var(--yellow)"/><path d="M6 11.5 L9.5 15 L16 7.5" fill="none" stroke="var(--black)" stroke-width="2.4"/></svg>Vacuum Boosters</li>
        <li><svg width="22" height="22" viewBox="0 0 22 22" aria-hidden="true"><circle cx="11" cy="11" r="10" fill="var(--yellow)"/><path d="M6 11.5 L9.5 15 L16 7.5" fill="none" stroke="var(--black)" stroke-width="2.4"/></svg>Remotes Boosters</li>
      </ul>
      <p class="range-note">Also supply parts<br>and kits etc.</p>
    </section>

    <address class="contact contact-left">
      <div class="contact-row">
        <svg width="20" height="20" viewBox="0 0 20 20" aria-hidden="true"><circle cx="10" cy="10" r="9.5" fill="var(--yellow)"/><path d="M10 4.5 a3.5 3.5 0 0 1 3.5 3.5 c0 2.5 -3.5 6.5 -3.5 6.5 s-3.5 -4 -3.5 -6.5 a3.5 3.5 0 0 1 3.5 -3.5 z" fill="none" stroke="var(--black)" stroke-width="1.3"/><circle cx="10" cy="8" r="1.2" fill="var(--black)"/></svg>
        18 Kowhai Lane, Hamilton
      </div>
      <div class="contact-row">
        <svg width="20" height="20" viewBox="0 0 20 20" aria-hidden="true"><circle cx="10" cy="10" r="9.5" fill="var(--yellow)"/><rect x="5" y="6.5" width="10" height="7" fill="none" stroke="var(--black)" stroke-width="1.3"/><path d="M5 6.5 L10 10.5 L15 6.5" fill="none" stroke="var(--black)" stroke-width="1.3"/></svg>
        parts@brellonmotorhub.co.nz
      </div>
      <div class="contact-row">
        <svg width="20" height="20" viewBox="0 0 20 20" aria-hidden="true"><circle cx="10" cy="10" r="9.5" fill="var(--yellow)"/><circle cx="10" cy="10" r="5" fill="none" stroke="var(--black)" stroke-width="1.2"/><ellipse cx="10" cy="10" rx="2.2" ry="5" fill="none" stroke="var(--black)" stroke-width="1.1"/><path d="M5 10 H15" stroke="var(--black)" stroke-width="1.1"/></svg>
        www.brellonmotorhub.co.nz
      </div>
    </address>

    <div class="footer-brand">BRELLON<br>MOTOR HUB</div>

    <address class="contact contact-right">
      <div class="contact-row">
        <svg width="20" height="20" viewBox="0 0 20 20" aria-hidden="true"><circle cx="10" cy="10" r="9.5" fill="var(--yellow)"/><path d="M6.5 5.5 l2 0 l1 2.5 l-1.3 1 a6 6 0 0 0 2.8 2.8 l1 -1.3 l2.5 1 l0 2 a1 1 0 0 1 -1 1 a8.5 8.5 0 0 1 -8 -8 a1 1 0 0 1 1 -1 z" fill="var(--black)"/></svg>
        Free Phone - 0800 55 41 82
      </div>
      <div class="contact-row no-icon">Ph 07 555 0143 | Fax 07 555 0144</div>
      <div class="unsubscribe">Unsubscribe from this list</div>
    </address>
  </main>
</body>
</html>
```